Consultancy Business Card Design

We need a business card design for a new company based in singapore called FortyOne. FortyOne a boutique consultancy firm offering broad-based business solutions, from conception to re-invention, for ventures from new start-ups to long-running traditional businesses.
Its 2 main divisions (Food & Beverage Operations and Construction & Project Management) have access to a wide range of networks, knowledge bases, and resources to service its clients across numerous diverse sectors. This includes, and is not limited to, construction, F&B, and retail.
We are a company that combines the ambition, boldness and energy of one in the 20s with the dedication, level-headedness and dependability of one entering its 30s. Bridging the experiences of the old with ideals of the young, we draw on the positives of both to create a unique synergy.
We hope to see designs that fits our company profile.
Boutique
FortyOne(Company Name)
Marcus Leow (Name)
Principle Consultant (Title)
F&B and Hospitality (Division)
(+65) 8364 5170 (Contact no.)
marcus@fortyone-example.com.sg (Email)

```html
<!DOCTYPE html>
<html lang="en">
<head>
<meta charset="utf-8">
<title>FortyOne Business Card</title>
<link rel="stylesheet" href="https://fonts.googleapis.com/css2?family=Open+Sans:wght@400;600;700&display=swap">
<style>
  :root {
    --backdrop: #d9d6d1;
    --card-white: #ffffff;
    --card-black: #121212;
    --ink: #2a2a2a;
    --ink-soft: #6a6a6a;
    --accent-red: #d62a45;
    --accent-red-deep: #b81f38;
    --type: "Open Sans", Arial, sans-serif;
  }
  * { box-sizing: border-box; margin: 0; padding: 0; }
  html, body {
    width: 1200px; height: 1023px; overflow: hidden;
    background: var(--backdrop);
    font-family: var(--type);
  }
  .canvas { position: relative; width: 1200px; height: 1023px; }
  .card {
    position: absolute; left: 250px; width: 700px; height: 400px;
    overflow: hidden;
    box-shadow: 0 10px 28px rgba(0,0,0,.25);
  }
  .card--front { top: 90px; background: var(--card-white); }
  .card--back {
    top: 533px;
    background: linear-gradient(135deg, #2b2b2b 0%, var(--card-black) 55%, #050505 100%);
  }

  .accent-area {
    position: absolute; width: 170px; height: 170px;
    background: linear-gradient(135deg, var(--accent-red) 0%, var(--accent-red-deep) 100%);
  }
  .accent-area--lower { left: 0; bottom: 0; }
  .accent-area--upper { right: 0; top: 0; }

  .contact {
    position: absolute; left: 215px; top: 92px; width: 300px;
    color: var(--ink);
  }
  .contact__name {
    font-size: 27px; font-weight: 700; letter-spacing: .5px;
    color: var(--accent-red); text-transform: uppercase; line-height: 1.1;
  }
  .contact__title { font-size: 14px; color: var(--ink-soft); margin-top: 4px; }
  .contact__phone { font-size: 18px; margin-top: 26px; }
  .contact__email { font-size: 17px; margin-top: 12px; }
  .contact__division { font-size: 18px; margin-top: 34px; }

  .brand { position: absolute; left: 0; right: 0; top: 118px; text-align: center; }
  .brand__name {
    font-size: 92px; font-weight: 600; color: #ffffff;
    letter-spacing: -1px; line-height: 1;
  }
  .brand__divisions {
    margin-top: 22px; font-size: 18px; color: #f0f0f0; letter-spacing: .3px;
  }
  .brand__web {
    position: absolute; left: 34px; bottom: 28px;
    font-size: 15px; color: #cfcfcf; letter-spacing: 1px;
  }
</style>
</head>
<body>
<main class="canvas">
  <section class="card card--front" aria-label="Business card front">
    <div class="accent-area accent-area--lower" role="img" aria-label="Red corner graphic"></div>
    <div class="accent-area accent-area--upper" role="img" aria-label="Red corner graphic"></div>
    <div class="contact">
      <h1 class="contact__name">Marcus Leow</h1>
      <p class="contact__title">Principle Consultant</p>
      <p class="contact__phone">(+65) 8364 5170</p>
      <p class="contact__email">marcus@fortyone-example.com.sg</p>
      <p class="contact__division">F&amp;B and Hospitality</p>
    </div>
  </section>

  <section class="card card--back" aria-label="Business card back">
    <div class="brand">
      <p class="brand__name">FortyOne</p>
      <p class="brand__divisions">Food &amp; Beverage Operations | Construction &amp; Project Management</p>
    </div>
    <p class="brand__web">www.fortyone-example.com.sg</p>
  </section>
</main>
</body>
</html>
```